Sleek, Professional Business Card Design Needed

Business Cards - Logo Attached.

We are a solar consulting company. We are national and want our cards to represent the professional high quality products that we offer.

Industry/Entity Type

Business

Contact Information for Business Card

n/a

Requirements
Must have
• Design
• Name
• Position
• Number
• Email
• Address
Should not have
• Not be too crowded

```html
<!DOCTYPE html>
<html lang="en">
<head>
<meta charset="utf-8">
<title>Sun Harbor Energy – Business Card</title>
<link rel="stylesheet" href="https://fonts.googleapis.com/css2?family=Open+Sans:wght@400;600;700&display=swap">
<style>
  :root {
    --backdrop: #04334a;
    --card: #ffffff;
    --brand-blue: #1a8fd0;
    --brand-blue-light: #5bbbe8;
    --brand-green: #8cc63f;
    --pattern-grey: #eef1f4;
  }
  * { margin: 0; padding: 0; box-sizing: border-box; }
  html, body {
    width: 1200px; height: 1000px; overflow: hidden;
    background: var(--backdrop);
    font-family: "Open Sans", sans-serif;
  }
  .business-card {
    position: absolute; left: 100px; top: 214px;
    width: 1000px; height: 571px;
    border-radius: 46px; overflow: hidden;
    background: var(--card);
  }
  .card-art { position: absolute; inset: 0; width: 100%; height: 100%; }
  .brand {
    position: absolute; left: 48px; top: 150px;
    display: flex; align-items: center; gap: 16px;
  }
  .brand-dot {
    width: 44px; height: 44px; border-radius: 50%;
    background: var(--brand-green);
  }
  .brand-name {
    font-size: 36px; font-weight: 600; color: var(--brand-blue);
    letter-spacing: 0.5px; text-transform: uppercase;
  }
  .contact {
    position: absolute; right: 42px; top: 250px;
    text-align: right; color: var(--brand-blue);
  }
  .person-name { font-size: 35px; font-weight: 400; letter-spacing: 1px; line-height: 1.1; }
  .person-name strong { font-weight: 700; }
  .person-role { font-size: 25px; font-weight: 600; color: var(--brand-green); letter-spacing: 1px; line-height: 1.1; margin-top: 2px; }
  .details { margin-top: 26px; list-style: none; }
  .details li {
    display: flex; justify-content: flex-end; align-items: center; gap: 12px;
    font-size: 25px; font-weight: 600; line-height: 35px;
  }
  .details .icon { width: 24px; height: 24px; flex: none; }
  .address { margin-top: 12px; font-size: 25px; font-weight: 600; line-height: 33px; padding-right: 36px; }
</style>
</head>
<body>
  <section class="business-card">
    <svg class="card-art" viewBox="0 0 1000 571" preserveAspectRatio="none">
      <polygon role="img" aria-label="Light dotted grid texture" points="30,571 1000,45 1000,571" fill="var(--pattern-grey)"/>
      <polygon class="swoosh-green" points="380,336 980,22 1000,10 1000,40" fill="var(--brand-green)"/>
      <polygon class="swoosh-blue" points="0,528 985,52 1000,56 20,571 0,571" fill="var(--brand-blue)"/>
      <polygon class="swoosh-blue-light" points="14,571 990,62 1000,66 40,571" fill="var(--brand-blue-light)"/>
    </svg>

    <div class="brand">
      <span class="brand-dot"></span>
      <span class="brand-name">Sun Harbor Energy</span>
    </div>

    <div class="contact">
      <p class="person-name"><strong>ALAN</strong> PORTER</p>
      <p class="person-role">owner</p>
      <ul class="details">
        <li>555 010 2468
          <svg class="icon" viewBox="0 0 24 24"><path d="M3 9c0-3 4-5 9-5s9 2 9 5l-4 1-1-2c-2-1-6-1-8 0l-1 2z M6 12h12l2 8H4z" fill="var(--brand-green)"/><circle cx="12" cy="16" r="2.5" fill="#fff"/></svg>
        </li>
        <li>AlanPorter@email.com
          <svg class="icon" viewBox="0 0 24 24"><rect x="2" y="5" width="20" height="14" fill="var(--brand-green)"/><path d="M2 5l10 8 10-8" fill="none" stroke="#fff" stroke-width="2"/></svg>
        </li>
        <li>www.sunharborenergy.com
          <svg class="icon" viewBox="0 0 24 24"><circle cx="12" cy="12" r="10" fill="var(--brand-green)"/><path d="M12 2v20M2 12h20M12 2c-5 5-5 15 0 20M12 2c5 5 5 15 0 20" fill="none" stroke="#fff" stroke-width="1.5"/></svg>
        </li>
      </ul>
      <p class="address">4821 Harbor Ln #210<br>Linden Bay, FL 33001</p>
    </div>
  </section>
</body>
</html>
```